Visitenkarten-Design für German Consulting Company
Zielgruppe
We are a German Consulting Company, who specialized in public sector Software development (www.qrt-beratung.de).
Our customers are audit offices all over Germany. We offer 3 custom software solution’s to our customers. Those three software solutions form a Software-Suite.
Our three products are called: qrt clearScope, qrt ledgerPilot and qrt ledgerWriter..
You can find the 3 Logos for our products enclosed
Wir sind eine Unternehmensberatung, die sich auf Softwareentwicklung für den Public Sektor spezialisiert hat (www.qrt-beratung.de). Unsere Zielgruppe sind Rechnungsprüfungsämter in ganz Deutschland. Wir bieten für diesen Markt drei abgestimmte Softwareprodukte an, die zusammen eine Software-Suite bilden. Die drei Produkte sind der qrt clearScope, der qrt ledgerWriter und der qrt ledgerPilot.
Aufgabenstellung
For activation, our software needs a licence key. This Key is sent to our customers with a nice box an the requird documentation.
The licence Key is supposed to be printed onto a metal card.
We are looking for a design regarding those „licencecards“
You can find the avaliable options for materials and customizations here: https://www.karten-stahl-vp.example/optionen/
The card has at least to show the following Information’s:
Company Logo and
licencekey: 8416 9072 5831 6049
We are going for a clean, professional and high value look.
Unsere Produkte benötigen einen Lizenzschlüssel um aktiviert zu werden. Dieser Lizenzschlüssel wird mit den dazugehörigen Handbüchern in einer edlen Verpackung übergeben. Der Lizenzschlüssel soll auf einer Metallkarte aufgebracht werden, wie Sie diese Firma anbietet: https://www.karten-stahl-vp.example/.
Materialien und Verabreitungsmöglichkeiten werden hier aufgeführt: https://www.karten-stahl-vp.example/optionen/
Die Karte muss mindestens unser Firmenlogo und eine 16 Stellige Lizenznummer(8416 9072 5831 604) enthalten.
Die Karte soll clean, professionell und hochwertig aussehen und wenige Farben verwenden .

```html
<!DOCTYPE html>
<html lang="de">
<head>
<meta charset="utf-8">
<title>Lizenzkarte – qrt</title>
<link rel="stylesheet" href="https://fonts.googleapis.com/css2?family=Michroma&display=swap">
<style>
  :root {
    --backdrop: #141414;
    --card-light: #2e2e2e;
    --card-dark: #1c1c1c;
    --ink: #f2f2f2;
    --accent: #d0161b;
  }
  html, body {
    margin: 0;
    padding: 0;
    width: 1200px;
    height: 912px;
    overflow: hidden;
    background: var(--backdrop);
  }
  .sheet {
    position: relative;
    width: 1200px;
    height: 912px;
  }
  .card {
    position: absolute;
    width: 520px;
    height: 336px;
    border-radius: 4px;
    background: linear-gradient(160deg, var(--card-light) 0%, var(--card-dark) 100%);
    box-shadow: 0 14px 34px rgba(0,0,0,0.6);
    font-family: "Michroma", sans-serif;
    color: var(--ink);
  }
  .card--front { left: 90px; top: 130px; }
  .card--back  { left: 590px; top: 446px; }

  .brand {
    position: absolute;
    left: 70px;
    top: 146px;
    display: flex;
    align-items: center;
    gap: 14px;
  }
  .brand__square {
    width: 34px;
    height: 34px;
    background: var(--accent);
  }
  .brand__name {
    font-size: 17px;
    letter-spacing: 0.5px;
    color: var(--ink);
  }

  .licence {
    position: absolute;
    left: 0;
    right: 0;
    top: 100px;
    text-align: center;
  }
  .licence__label {
    font-size: 13px;
    letter-spacing: 1px;
    margin-bottom: 14px;
  }
  .licence__key {
    font-size: 25px;
    letter-spacing: 2px;
  }
  .licence__web {
    position: absolute;
    left: 0;
    right: 0;
    bottom: 56px;
    text-align: center;
    font-size: 12px;
    letter-spacing: 1px;
  }
</style>
</head>
<body>
  <main class="sheet">
    <section class="card card--front" aria-label="Vorderseite">
      <div class="brand">
        <span class="brand__square"></span>
        <span class="brand__name">qrt quast, reinholt &amp; thiel</span>
      </div>
    </section>

    <section class="card card--back" aria-label="Rückseite">
      <div class="licence">
        <div class="licence__label">LICENCE KEY:</div>
        <div class="licence__key">8416 9072 5831 6049</div>
      </div>
      <div class="licence__web">www.qrt-beratung.de</div>
    </section>
  </main>
</body>
</html>
```